Promotion material for corporate wellness firm.

I am looking to have a flyer designed that gives some background on the company offerings for corporate wellness. I have attached the content and logo files I would like included and a photo of Meg but if there are other relevant nutrition related photos we would be open to have those included. We are looking for professional but a little light.

Target Market(s)

corporate officers.

Industry/Entity Type

It Company

```html
<!DOCTYPE html>
<html lang="en">
<head>
<meta charset="utf-8">
<title>Meg Harwell Wellness – Corporate Wellness Brochure</title>
<link href="https://fonts.googleapis.com/css2?family=Montserrat:wght@400;500;600;700&family=Raleway:wght@300;400;500&display=swap" rel="stylesheet">
<style>
  :root{
    --backdrop:#1f1f1f;
    --paper:#ffffff;
    --green:#2e9a3a;
    --green-dark:#1f7a2b;
    --grey-band:#c9c9c9;
    --ink:#444444;
    --ink-soft:#666666;
    --photo-warm:#c9b7a3;
    --photo-blue:#4a55a6;
    --photo-food:#7fae4f;
  }
  *{box-sizing:border-box;margin:0;padding:0}
  html,body{width:1200px;height:1200px;overflow:hidden;background:var(--backdrop)}
  body{position:relative;font-family:"Raleway",sans-serif;color:var(--ink)}
  .page{position:absolute;width:417px;height:542px;background:var(--paper);overflow:hidden}
  .page--cover{left:181px;top:57px}
  .page--about{left:602px;top:57px}
  .page--approach{left:181px;top:602px}
  .page--services{left:602px;top:602px}
  .page svg.bg{position:absolute;left:0;top:0;width:100%;height:100%}
  .abs{position:absolute}
  .brand-tag{position:absolute;top:28px;right:24px;font-family:"Montserrat",sans-serif;font-size:6px;letter-spacing:.4px;color:var(--ink-soft);display:flex;align-items:center;gap:4px}
  .brand-tag .dot{width:5px;height:5px;border-radius:50%;background:var(--green)}
  .page-no{position:absolute;right:24px;bottom:20px;font-size:6px;color:var(--green);font-family:"Montserrat",sans-serif}
  .page-no span{margin-left:6px}

  /* cover */
  .cover-name{position:absolute;left:26px;top:350px;border-left:4px solid #fff;padding-left:9px;color:#fff}
  .cover-name h1{font-family:"Montserrat",sans-serif;font-weight:600;font-size:25px;line-height:28px}
  .cover-name p{font-size:12px;font-weight:400;letter-spacing:.5px}
  .cover-brand{position:absolute;left:236px;top:466px;width:166px;text-align:center;font-family:"Montserrat",sans-serif;color:#555;white-space:nowrap}
  .cover-brand .word{font-size:19px;font-weight:500;letter-spacing:.3px;line-height:24px}
  .cover-brand .sub{font-size:10px;font-weight:600;letter-spacing:3px;margin-top:6px}
  .cover-contact{position:absolute;left:26px;top:494px;font-size:10.5px;color:#444;display:flex;align-items:center;gap:4px}
  .cover-contact svg{width:12px;height:12px}

  /* about */
  .about-name{position:absolute;left:37px;top:58px;width:145px;color:#fff}
  .about-name h1{font-family:"Montserrat",sans-serif;font-weight:500;font-size:21px;line-height:28px;white-space:nowrap}
  .about-name p{font-size:11px;letter-spacing:.4px}
  .credentials{position:absolute;left:37px;top:330px;width:140px;color:#fff}
  .credentials h3{font-family:"Montserrat",sans-serif;font-size:8.5px;font-weight:600;margin-bottom:5px}
  .credentials ul{list-style:none}
  .credentials li{font-size:7.4px;line-height:11.5px;padding-left:10px;position:relative;margin-bottom:4px}
  .credentials li::before{content:"•";position:absolute;left:0}
  .about-copy{position:absolute;left:197px;top:304px;width:196px;font-size:6.6px;line-height:9.6px;text-align:justify}
  .about-copy .lead{color:var(--green);font-weight:500;margin-bottom:5px}
  .about-copy p{margin-bottom:5px}

  /* shared section styling */
  .col{position:absolute;width:170px}
  .heading{font-family:"Montserrat",sans-serif;font-weight:700;color:var(--green);font-size:12.5px;line-height:15px;border-left:3px solid var(--green);padding-left:6px;margin-bottom:4px;text-transform:uppercase}
  .body{font-size:6.6px;line-height:9.6px;color:var(--ink-soft);margin-bottom:12px}
  .intro{font-family:"Montserrat",sans-serif;font-weight:600;color:var(--green-dark);font-size:9px;line-height:13.5px;margin-bottom:12px}
  .believe{position:absolute;left:25px;top:420px;color:#fff;font-family:"Montserrat",sans-serif}
  .believe h3{font-size:12px;font-weight:600;margin-bottom:3px}
  .believe li{list-style:none;font-size:7.4px;line-height:12px;font-weight:500;padding-left:9px;position:relative}
  .believe li::before{content:"•";position:absolute;left:0}

  /* services */
  .services-title{position:absolute;left:25px;top:88px;color:#fff;font-family:"Montserrat",sans-serif;font-weight:600;font-size:26px;line-height:27px}
  .services-lead{position:absolute;left:25px;top:208px;width:370px;font-family:"Montserrat",sans-serif;font-weight:600;color:var(--green-dark);font-size:8.8px;line-height:13px}
  .sub-title{font-family:"Montserrat",sans-serif;font-weight:600;font-size:8.6px;color:#333;text-transform:uppercase;margin-bottom:2px}
  .svc .body{font-size:6.2px;line-height:8.8px;margin-bottom:7px}
</style>
</head>
<body>

<!-- Page 01: cover -->
<section class="page page--cover">
  <svg class="bg" viewBox="0 0 417 542" aria-hidden="true">
    <path d="M0 300 C140 350 310 300 417 200 V310 C320 420 170 455 0 468 Z" fill="var(--green)"/>
    <path d="M0 475 C180 462 320 420 417 340 V348 C320 428 180 470 0 484 Z" fill="var(--grey-band)"/>
  </svg>
  <svg class="abs" style="left:0;top:0" width="417" height="340" viewBox="0 0 417 340" role="img" aria-label="Photo of Meg Harwell smiling in a kitchen beside a counter of fresh fruit and vegetables">
    <defs>
      <linearGradient id="coverPhoto" x1="0" y1="0" x2="1" y2="1">
        <stop offset="0" stop-color="#e8e1d6"/>
        <stop offset=".45" stop-color="var(--photo-warm)"/>
        <stop offset=".75" stop-color="var(--photo-blue)"/>
        <stop offset="1" stop-color="#5d6c3a"/>
      </linearGradient>
    </defs>
    <path d="M0 0 H417 V195 C320 320 150 345 0 300 Z" fill="url(#coverPhoto)"/>
  </svg>
  <div class="cover-name">
    <h1>Meg Harwell</h1>
    <p>M.B.A., R.D., L.D.N.</p>
  </div>
  <div class="cover-brand">
    <div class="word">MEG HARWELL</div>
    <div class="sub">WELLNESS</div>
  </div>
  <div class="cover-contact">
    <svg viewBox="0 0 24 24"><circle cx="12" cy="12" r="10.5" fill="none" stroke="#444" stroke-width="1.6"/><path d="M8.5 7c.6-.5 1.3-.4 1.7.2l1 1.5c.3.5.2 1-.2 1.4l-.6.5c.6 1.3 1.6 2.3 2.9 2.9l.5-.6c.4-.4.9-.5 1.4-.2l1.5 1c.6.4.7 1.1.2 1.7-1 1.1-2.6 1.300-4 .5a11 11 0 0 1-4.600-4.600c-.8-1.400-.6-3 .5-4z" fill="#444"/></svg>
    <span>555-010-2468</span>
    <svg viewBox="0 0 24 24"><circle cx="12" cy="12" r="10.5" fill="none" stroke="#444" stroke-width="1.6"/><rect x="6.5" y="8" width="11" height="8" rx="1" fill="none" stroke="#444" stroke-width="1.4"/><path d="M6.5 8.5 12 12.5l5.5-4" fill="none" stroke="#444" stroke-width="1.4"/></svg>
    <span>hello@megharwell.com</span>
  </div>
</section>

<!-- Page 02: about -->
<section class="page page--about">
  <svg class="bg" viewBox="0 0 417 542" aria-hidden="true">
    <rect x="25" y="0" width="161" height="542" fill="var(--green)"/>
  </svg>
  <svg class="abs" style="left:0;top:0" width="417" height="542" viewBox="0 0 417 542" role="img" aria-label="Portrait photo of Meg Harwell in a blue top, smiling">
    <defs>
      <linearGradient id="aboutPhoto" x1="0" y1="0" x2="1" y2="0">
        <stop offset="0" stop-color="#8a7360"/>
        <stop offset=".5" stop-color="#d8c7ae"/>
        <stop offset="1" stop-color="var(--photo-warm)"/>
      </linearGradient>
    </defs>
    <polygon points="25,159 392,41 392,227 25,323" fill="url(#aboutPhoto)"/>
  </svg>
  <div class="brand-tag"><span class="dot"></span>MEG HARWELL WELLNESS</div>
  <div class="about-name">
    <h1>Meg Harwell</h1>
    <p>M.B.A., R.D., L.D.N.</p>
  </div>
  <div class="credentials">
    <h3>CREDENTIALS:</h3>
    <ul>
      <li>B.S. in Human Nutrition, and Exercise and Fitness From Lakeshore State University</li>
      <li>Dietetic Residency, M.B.A. in Healthcare Administration from Westbrook University, Elm Grove, IL</li>
      <li>Memberships: National Dietetics Association, Food Business Circle, Dietitians in Media and Enterprise, and the Healthy Weight Practice Network</li>
    </ul>
  </div>
  <div class="about-copy">
    <p class="lead">Meg has worked in the health and fitness industry for over a decade. As a registered dietitian, she uses evidence-based strategies to help clients make dietary changes to improve overall health and well-being. As a fitness instructor, Meg truly embodies the concept of health and wellness and emphasizes the important relationship between nutrition and exercise.</p>
    <p>Meg's passion for her work allows her to forge connections and motivate her clients to reach their health and wellness goals. She eagerly shares her expertise in healthy living with clients at every point of their life cycle. Meg believes that everyone can feel better and more energetic by incorporating healthy living strategies into every day life. Some areas of particular interest include overall wellness, weight loss, sports nutrition, prevention of cardiovascular disease, diabetes and gastro-intestinal diseases, and understanding food allergies.</p>
    <p>Meg stays active and healthy by running and cycling, gardening and baking, and enjoys adventures with her family and friends.</p>
  </div>
  <div class="page-no">Page<span>02</span></div>
</section>

<!-- Page 03: approach -->
<section class="page page--approach">
  <svg class="bg" viewBox="0 0 417 542" aria-hidden="true">
    <path d="M0 340 C120 400 300 390 417 310 V542 H0 Z" fill="var(--green)"/>
    <path d="M0 490 C150 530 320 500 417 380 V400 C330 520 160 545 0 505 Z" fill="var(--paper)"/>
    <path d="M0 510 C160 548 330 520 417 410 V542 H0 Z" fill="var(--grey-band)"/>
    <path d="M0 532 C160 560 330 540 417 440 V542 H0 Z" fill="var(--paper)"/>
  </svg>
  <div class="brand-tag"><span class="dot"></span>MEG HARWELL WELLNESS</div>
  <div class="col" style="left:25px;top:52px">
    <p class="intro">I've always been interested in health and fitness. And, I genuinely love helping people. As a dietitian, I get to bring all my passions together.</p>
    <h2 class="heading">Dietitian or Nutritionist</h2>
    <p class="body">Dietitians, nutritionists, health coaches. It gets confusing, but there's a difference. A Registered Dietitian (that's me) is a food and nutrition professional who has met the academic and professional requirements for the credential. Registered Dietitians are the only licensed credentials recognized as providers of medical nutrition therapy (MNT).</p>
    <h2 class="heading">My Approach</h2>
    <p class="body">It's individualized because everyone's different. I start by getting to know my clients and their goals, challenges, health history and eating habits. This is important because it helps inform what strategies will work — and won't. Because I'm also fitness instructor, I provide a well-rounded approach that includes both exercise and eating strategies. And, the strategies I use are evidence-based — that's a fancy way of saying they're proven to be successful.</p>
  </div>
  <div class="col" style="left:217px;top:52px">
    <h2 class="heading">What is a Registered Dietitian?</h2>
    <p class="body">Dietitians, nutritionists, health coaches. It gets confusing, but there's a difference. A Registered Dietitian is a food and nutrition professional who has met the academic and professional requirements for the credential. Registered Dietitians are the only licensed credentials recognized as providers of medical nutrition therapy (MNT).</p>
    <h2 class="heading">Special Interest in Corporate Wellness</h2>
    <p class="body">I enjoy partnering with organizations who believe in health and wellness. I provide programs, tools and coaching that help employees identify and reach their goals. When employees are healthier, they're happier, more productive and have fewer sick days. Everybody benefits.</p>
    <h2 class="heading">The Perfect Client</h2>
    <p class="body">My clients are all different: People looking to lose weight, people looking to gain weight, diabetics, athletes, and so on. The one thing that they all have in common? They're truly engaged and motivated. That's what makes it work.</p>
  </div>
  <svg class="abs" style="left:193px;top:355px" width="160" height="160" viewBox="0 0 160 160" role="img" aria-label="Round photo of a smiling woman eating a fresh salad">
    <defs>
      <radialGradient id="saladWoman" cx=".4" cy=".4" r=".7">
        <stop offset="0" stop-color="#d9b79a"/>
        <stop offset=".6" stop-color="var(--photo-food)"/>
        <stop offset="1" stop-color="#4f8a37"/>
      </radialGradient>
    </defs>
    <circle cx="80" cy="80" r="78" fill="#e5e5e5"/>
    <circle cx="80" cy="80" r="73" fill="url(#saladWoman)"/>
  </svg>
  <div class="believe">
    <h3>WHAT I BELIEVE</h3>
    <ul>
      <li>Diets don't work.</li>
      <li>Nutrition is personal and individual.</li>
      <li>Potato chips should not be banned.</li>
      <li>There's no one-size-fits-all nutrition plan.</li>
      <li>I can help anybody who's up for it.</li>
    </ul>
  </div>
  <div class="page-no">Page<span>03</span></div>
</section>

<!-- Page 04: services -->
<section class="page page--services">
  <svg class="bg" viewBox="0 0 417 542" aria-hidden="true">
    <path d="M0 0 H230 C300 14 370 34 417 46 V70 C330 150 170 172 0 160 Z" fill="var(--green)"/>
    <path d="M0 165 C170 178 330 155 417 76 V96 C330 175 170 198 0 195 Z" fill="var(--grey-band)"/>
  </svg>
  <div class="brand-tag"><span class="dot"></span>MEG HARWELL WELLNESS</div>
  <svg class="abs" style="left:200px;top:45px" width="145" height="145" viewBox="0 0 145 145" role="img" aria-label="Round photo of a bowl of fresh mixed salad with tomatoes, corn and cheese">
    <defs>
      <radialGradient id="saladBowl" cx=".5" cy=".5" r=".6">
        <stop offset="0" stop-color="#f1e7c8"/>
        <stop offset=".5" stop-color="var(--photo-food)"/>
        <stop offset="1" stop-color="#b64a32"/>
      </radialGradient>
    </defs>
    <circle cx="72.5" cy="72.5" r="71" fill="#e5e5e5"/>
    <circle cx="72.5" cy="72.5" r="66" fill="url(#saladBowl)"/>
  </svg>
  <h1 class="services-title">OUR<br>SERVICES</h1>
  <p class="services-lead">Whether it's working with individuals or large companies, the goal is the same: helping people live healthier lives.</p>
  <div class="col svc" style="left:25px;top:241px;width:177px">
    <h2 class="heading" style="margin-bottom:9px">Corporate Wellness Services</h2>
    <h3 class="sub-title">Initial Consultation</h3>
    <p class="body">60-minute consultation with employees, including a full nutrition assessment to understand their health history, current eating habits and goals for moving forward. Employees receive a personalized plan with strategies and tools for success. Consults are held in person, over the phone or via video messaging.</p>
    <h3 class="sub-title">Follow-Up Consultation</h3>
    <p class="body">30-minute consultation with employees to evaluate progress toward goals, provide guidance, and to develop new strategies if needed. Consults are held in person, over the phone or via video messaging.</p>
    <h3 class="sub-title">Workplace Events</h3>
    <p class="body">Coordination of workplace challenges, wellness screenings, lifestyle management programs or other engaging health events that are fun and inspire employees to stay on track toward reaching their goals.</p>
    <h3 class="sub-title">Group Nutrition Presentations</h3>
    <p class="body">Group speaking events or lunch-and-learns to educate employees about nutrition, health and wellness. Popular topics include: Meal Planning Made Easy, Healthy Holiday Eating, Stress Management, Eating Well on the Road, and Dining Out.</p>
  </div>
  <div class="col svc" style="left:217px;top:241px;width:177px">
    <h3 class="sub-title">Cooking Demonstrations</h3>
    <p class="body" style="margin-bottom:18px">Live cooking demonstrations where employees learn how to cook delicious meals and snacks that are aligned with their dietary goals.</p>
    <h2 class="heading" style="margin-bottom:7px">Individual Services</h2>
    <h3 class="sub-title">Initial Consultation</h3>
    <p class="body">60-minute consultation, including a full nutrition assessment to understand client's health history, current eating patterns, and goals for moving forward. Client receives a personalized plan with strategies and tools for success. Consults are held in person, over the phone or via video messaging.</p>
    <h3 class="sub-title">Follow-Up Consultations</h3>
    <p class="body">30-minute consultation with clients to evaluate progress toward goals, provide guidance, and to develop new strategies if needed. Consults are held in person, over the phone or via video messaging.</p>
    <h3 class="sub-title">Grocery Store Tours</h3>
    <p class="body">60-minute guided tour of the store, providing education about a variety of healthy foods, how to read and understand nutrition labels and claims, and meal-planning tips.</p>
  </div>
  <div class="page-no">Page<span>04</span></div>
</section>

</body>
</html>
```